High-end executive coaching group needs a 2 page digital flyer

We need a 2 page digital flyer for a high end leadership coaching offering for global leaders in healthcare. The flyer will advertise a new service (an elite senior leadership coaching group) for senior leaders in the healthcare industry from around the world.
The flyer should be upmarket, professional and minimalist in style to meet the expectations of my professional market (very senior doctors and executives).
The design should be based on my existing logo and brand, see my landing page: www.marlowadvisory.com
The key elements needed are
1) An editable PDF which we can update as we revise the specific details of the offering. The text and draft design for this is attached.
2) The banner image should be high quality but abstract. It can be based on the landing page of my website (the two ripple effects) but does not need to strictly adhere to this.
3) The logo placement of the Marlow Advisory delta sign should be discreet so that it does not dominate
4) The small logos of our professional accrediting organisations should be discreetly placed at the end and should not dominate. They might work best as mono icons in a footer (e.g. blue on a white background, or white on blue.
5) Please find enclosed a previous flyer as an example of a similar style we have used for more junior professionals. The design worked quite well, although we now need a more upmarket version for our senior executives.
Updates

Please note this design specifically needs to use existing branding and images from my website: marlowadvisory.com. We are definitely not looking for stock "leadership team" images for this high-end brochure.

Target Market(s)

Senior global leaders in the healthcare industry

Industry/Entity Type

Leading business schools & Healthcare industry.

Font styles to use
Other font styles liked:
• Operetta (selective use for heading) and Sofia Pro (body text)

Colors
0054AA
0677BA
7BADD7
CADEEF
E8F1F8

Requirements
Must have
• Clean minimalist and high professionally look that directly speaks to the interests and perspectives of senior leader leaders in healthcare. It also needs very clear call to action sections
Nice to have
• Effective presentation of the two bios and photographs. These need to look impressive, but should not dominate.
Should not have
• Loud and bold colours, large use of logos.

```html
<!DOCTYPE html>
<html lang="en">
<head>
<meta charset="utf-8">
<title>Marlow Advisory – Senior Leadership Coaching</title>
<link href="https://fonts.googleapis.com/css2?family=Playfair+Display:ital,wght@0,600;1,500;1,600&family=Mulish:wght@400;600;700;800&display=swap" rel="stylesheet">
<style>
  :root{
    --navy:#0054AA;
    --blue:#0677BA;
    --sky:#7BADD7;
    --mist:#CADEEF;
    --ice:#E8F1F8;
    --ink:#1f2a3a;
    --white:#ffffff;
  }
  *{box-sizing:border-box;margin:0;padding:0}
  html,body{width:851px;height:1200px;overflow:hidden;background:var(--white)}
  .flyer{position:relative;width:851px;height:1200px;font-family:"Mulish",sans-serif;color:var(--ink)}
  .tagline{position:absolute;left:40px;top:26px;font-family:"Playfair Display",serif;font-style:italic;font-weight:500;font-size:23px;color:var(--navy)}
  .bios{position:absolute;left:0;top:72px;width:851px;height:590px;background:linear-gradient(160deg,var(--ice) 0%,var(--mist) 100%)}
  .photo{position:absolute;background:linear-gradient(150deg,var(--sky),var(--blue));}
  .photo-one{left:38px;top:20px;width:285px;height:240px}
  .photo-two{left:556px;top:300px;width:260px;height:236px}
  .bio{position:absolute;font-size:13.2px;line-height:18.5px;color:var(--ink)}
  .bio strong{color:var(--navy);font-weight:800}
  .bio-one{left:345px;top:26px;width:470px}
  .bio-two{left:40px;top:280px;width:495px}
  .questions{position:absolute;left:40px;top:690px;width:340px}
  .questions .lead{font-size:14.5px;line-height:20px;font-weight:600;color:var(--ink);margin-bottom:12px}
  .questions ul{list-style:none}
  .questions li{position:relative;padding-left:22px;font-size:13.6px;line-height:19px;font-weight:700;color:var(--navy);margin-bottom:14px}
  .questions li svg{position:absolute;left:0;top:3px}
  .quote{position:absolute;left:420px;top:668px;width:400px;height:260px}
  .quote .mark{position:absolute;font-family:"Playfair Display",serif;font-weight:600;font-size:88px;line-height:1;color:var(--blue)}
  .quote .open{left:0;top:0}
  .quote .close{right:0;bottom:-18px}
  .quote blockquote{position:absolute;left:52px;top:42px;width:330px;font-size:14.5px;line-height:21px;color:var(--ink)}
  .quote cite{position:absolute;left:52px;top:214px;font-style:normal;font-weight:700;font-size:14px;color:var(--navy)}
  .cta{position:absolute;left:0;top:950px;width:300px;height:250px;background:var(--navy);color:var(--white);padding:26px 30px}
  .cta h3{font-family:"Playfair Display",serif;font-style:italic;font-weight:600;font-size:19px;margin-bottom:6px}
  .cta p{font-size:13px;line-height:18px}
  .cta .book{margin-top:18px}
  .cta .book h3{margin-bottom:4px}
  .accredit{position:absolute;left:300px;top:950px;width:551px;height:132px;text-align:center}
  .accredit h4{margin-top:18px;font-family:"Playfair Display",serif;font-style:italic;font-weight:600;font-size:19px;color:var(--navy)}
  .badges{display:flex;justify-content:center;align-items:center;gap:26px;margin-top:14px}
  .badge{background:var(--mist)}
  .badge-circle{width:58px;height:58px;border-radius:50%;background:var(--navy)}
  .badge-rect{width:92px;height:46px;background:var(--sky)}
  .badge-wide{width:150px;height:46px;background:var(--mist)}
  .contact{position:absolute;left:300px;top:1082px;width:551px;height:118px;background:var(--blue);color:var(--white);padding:18px 26px}
  .contact h4{font-family:"Playfair Display",serif;font-style:italic;font-weight:600;font-size:22px;margin-bottom:10px}
  .contact .rows{display:grid;grid-template-columns:200px 1fr;row-gap:10px;font-size:13px;font-weight:600}
  .contact .item{display:flex;align-items:center;gap:8px}
  .contact .item svg{flex:none}
  .contact .brand{position:absolute;right:26px;top:22px;font-weight:700;font-size:14px}
</style>
</head>
<body>
<div class="flyer">
  <p class="tagline">Expertly guided by insight, academic rigour and practical leadership strategies</p>

  <section class="bios">
    <div class="photo photo-one" role="img" aria-label="Portrait photograph of Professor Daniel Hartley"></div>
    <p class="bio bio-one"><strong>Professor Daniel Hartley</strong> has 30 years' experience developing leaders. An award-winning business school professor, group analyst and psychoanalytic psychotherapist, he has taught senior leadership programmes at Ashbourne University, Kingsbridge College and the University of Carrow. His extensive leadership experience as a national health service clinical director and consultant psychotherapist informs his work as an IACC accredited executive coach. With a PhD from Whitmore College, University of Easton, he is an expert in melding psychological insights with strategic organisational change.</p>

    <p class="bio bio-two"><strong>Dr Helen Ashworth</strong> is a renowned psychoanalyst, group analyst, consultant psychiatrist and organisational consultant in the health sector. She has 20 years of leadership within the national health service and she was also the National Director of Therapies for the Larkfield Group, directing therapy services across 100 UK hospitals. She holds prominent positions as Chair of the Patient Safety Group, Chair of the Working Group on the Effect of Suicide and Homicide on Psychiatrists, and Vice Chair of the Psychotherapy Faculty at the Royal Society of Psychiatric Practice.</p>
    <div class="photo photo-two" role="img" aria-label="Portrait photograph of Dr Helen Ashworth"></div>
  </section>

  <section class="questions">
    <p class="lead">Engage with global leaders, gain diverse insights and forge lasting bonds. Explore questions such as:</p>
    <ul>
      <li><svg width="12" height="12" viewBox="0 0 12 12"><path d="M1 1 L11 6 L1 11 Z" fill="var(--sky)"/></svg>What kind of leader do I aspire to be in the next chapter of my life and career?</li>
      <li><svg width="12" height="12" viewBox="0 0 12 12"><path d="M1 1 L11 6 L1 11 Z" fill="var(--sky)"/></svg>What unique qualities and actions do I offer that no one else can?</li>
      <li><svg width="12" height="12" viewBox="0 0 12 12"><path d="M1 1 L11 6 L1 11 Z" fill="var(--sky)"/></svg>How can I galvanise my personal strengths to inspire and motivate others?</li>
    </ul>
  </section>

  <figure class="quote">
    <span class="mark open">&ldquo;</span>
    <blockquote>Through this exceptional coaching, our leadership team elevated its performance to lead the hospital with greater clarity, cohesion and thoughtfulness. Not only do we provide a superior work environment for staff, but better care for our patients.”</blockquote>
    <cite>– James, CEO</cite>
    <span class="mark close">&rdquo;</span>
  </figure>

  <section class="cta">
    <h3>Limited spots available</h3>
    <p>Don't miss this unique opportunity to transform your leadership journey.</p>
    <div class="book">
      <h3>Book your free discovery call</h3>
      <p>daniel@marlowadvisory.com<br>helen@marlowadvisory.com<br>www.marlowadvisory.com</p>
    </div>
  </section>

  <section class="accredit">
    <h4>Accredited by</h4>
    <div class="badges">
      <div class="badge badge-circle" role="img" aria-label="Accreditation badge"></div>
      <div class="badge badge-rect" role="img" aria-label="Accreditation badge"></div>
      <div class="badge badge-wide" role="img" aria-label="Accreditation badge"></div>
    </div>
  </section>

  <section class="contact">
    <h4>Contact Us</h4>
    <div class="rows">
      <div class="item">
        <svg width="20" height="20" viewBox="0 0 20 20"><circle cx="10" cy="10" r="10" fill="var(--white)"/><path d="M7 5.5c.5 0 1.5 2 1.5 2.5s-.8.8-.8 1.2c0 .8 1.8 2.6 2.6 2.6.4 0 .7-.8 1.2-.8s2.5 1 2.5 1.5c0 1-1 2-2 2-3 0-7-4-7-7 0-1 1-2 2-2z" fill="var(--blue)"/></svg>
        +61 3 9000 4821
      </div>
      <div class="item">
        <svg width="20" height="20" viewBox="0 0 20 20"><circle cx="10" cy="10" r="10" fill="var(--white)"/><rect x="5" y="6.5" width="10" height="7" fill="none" stroke="var(--blue)" stroke-width="1.3"/><path d="M5 6.5l5 4 5-4" fill="none" stroke="var(--blue)" stroke-width="1.3"/></svg>
        info@marlowadvisory.com
      </div>
      <div class="item">
        <svg width="20" height="20" viewBox="0 0 20 20"><circle cx="10" cy="10" r="10" fill="var(--white)"/><circle cx="10" cy="10" r="5" fill="none" stroke="var(--blue)" stroke-width="1.2"/><path d="M5 10h10M10 5c-2 2.5-2 7.5 0 10M10 5c2 2.5 2 7.5 0 10" fill="none" stroke="var(--blue)" stroke-width="1"/></svg>
        Marlow Advisory
      </div>
      <div class="item">
        <svg width="20" height="20" viewBox="0 0 20 20"><circle cx="10" cy="10" r="10" fill="var(--white)"/><circle cx="10" cy="10" r="5" fill="none" stroke="var(--blue)" stroke-width="1.2"/><path d="M5 10h10M10 5c-2 2.5-2 7.5 0 10M10 5c2 2.5 2 7.5 0 10" fill="none" stroke="var(--blue)" stroke-width="1"/></svg>
        www.marlowadvisory.com
      </div>
    </div>
  </section>
</div>
</body>
</html>
```